Private Investment Partnership needs Business Card Design

We are a brand-new private investment partnership looking for business card design help. It will be called The Corvale + Vantry Partnership. We are based in NYC (hence Corvale) and our other partner is a firm called Vantry Resources which has roots in Pittsburgh, PA. We are looking for something a bit more formal and professional- probably typographic oriented in a font like Adobe Garamond. We might want to incorporate the colors PMS Yellow 1235 and PMS Blue 282. Attached is a pretty plain, old example of something.

```html
<!DOCTYPE html>
<html lang="en">
<head>
<meta charset="utf-8">
<title>The Corvale + Vantry Partnership — Business Card</title>
<link rel="stylesheet" href="https://fonts.googleapis.com/css2?family=EB+Garamond:wght@400;500&display=swap">
<style>
  :root {
    --backdrop: #3a3a3a;
    --card-navy: #082a5e;
    --card-glow: #5b6273;
    --gold: #e9b23c;
    --card-w: 1100px;
    --card-h: 630px;
  }
  * { margin: 0; padding: 0; box-sizing: border-box; }
  html, body {
    width: 1200px;
    height: 1018px;
    overflow: hidden;
    background: var(--backdrop);
  }
  .canvas {
    position: relative;
    width: 1200px;
    height: 1018px;
  }
  .business-card {
    position: absolute;
    left: 50px;
    top: 194px;
    width: var(--card-w);
    height: var(--card-h);
    border-radius: 36px;
    background: radial-gradient(ellipse 46% 62% at 50% 38%, var(--card-glow) 0%, #33476b 45%, var(--card-navy) 100%);
    color: var(--gold);
    font-family: "EB Garamond", "Garamond", serif;
    overflow: hidden;
  }
  .holder-name {
    position: absolute;
    left: 44px;
    top: 222px;
    font-size: 42px;
    font-weight: 400;
    letter-spacing: 0.5px;
    line-height: 1;
  }
  .holder-title {
    position: absolute;
    left: 44px;
    top: 300px;
    font-size: 27px;
    line-height: 1;
  }
  .divider {
    position: absolute;
    left: 44px;
    right: 42px;
    top: 363px;
    height: 2px;
    background: var(--gold);
  }
  .contact-list {
    position: absolute;
    left: 44px;
    top: 424px;
    list-style: none;
    font-size: 24px;
    line-height: 1;
  }
  .contact-list li {
    display: flex;
    align-items: center;
    gap: 12px;
    height: 37px;
  }
  .contact-icon {
    width: 26px;
    height: 26px;
    flex: none;
    fill: var(--gold);
  }
  .company-name {
    position: absolute;
    left: 524px;
    top: 467px;
    transform: translateX(-50%);
    font-size: 25px;
    white-space: nowrap;
    line-height: 1;
  }
  .office-address {
    position: absolute;
    left: 791px;
    top: 450px;
    font-style: normal;
    font-size: 24px;
    line-height: 32px;
  }
</style>
</head>
<body>
<div class="canvas">
  <section class="business-card" aria-label="Business card">
    <h1 class="holder-name">DANIEL R. ASHCOMBE</h1>
    <p class="holder-title">Chief Investment Officer</p>
    <div class="divider"></div>

    <ul class="contact-list">
      <li>
        <svg class="contact-icon" viewBox="0 0 24 24" aria-hidden="true">
          <path d="M3 8c0-2 4-4 9-4s9 2 9 4v2h-5V8.5c-1-.6-2.4-.9-4-.9s-3 .3-4 .9V10H3z"/>
          <path d="M6 12h12l2 7H4z"/>
        </svg>
        <span>(212) 555-0148</span>
      </li>
      <li>
        <svg class="contact-icon" viewBox="0 0 24 24" aria-hidden="true">
          <path d="M8 2h8a2 2 0 0 1 2 2v16a2 2 0 0 1-2 2H8a2 2 0 0 1-2-2V4a2 2 0 0 1 2-2zm0 3v12h8V5zm4 13.2a1.2 1.2 0 1 0 0 2.4 1.2 1.2 0 0 0 0-2.4z"/>
        </svg>
        <span>(646) 555-0193</span>
      </li>
      <li>
        <svg class="contact-icon" viewBox="0 0 24 24" aria-hidden="true">
          <path d="M2 6h20v13H2zm2 2v.4l8 5.3 8-5.3V8z"/>
        </svg>
        <span>dashcombe@corvalevantry.com</span>
      </li>
    </ul>

    <p class="company-name">The Corvale + Vantry Partnership</p>

    <address class="office-address">
      240 Madison Avenue<br>
      New York, NY 10016
    </address>
  </section>
</div>
</body>
</html>
```